New business needs it's first website designed and coded for Wordpress

This is a new website for a new business. The business is called The Remote Tech Specialist (TRTS). The business is based across multiple countries with the goal of providing workers in the Philippines opportunities to find work in international companies based in Australia, Singapore and New Zealand. The target market for TRTS is large enterprises (initially in Australia) looking for well legally structured business that knows how to recruit the top IT professionals and ensure that they are happy, all compliance, taxes and legals and professionally done and all services contracts are local to ensure enforceability.

We are looking for 10 pages (6 templates) for the website as follows:
Home
About Us
Services
Work from home full-timers
Work from office full-times
Work from home contractors
Work from office contractors
Careers Job Search
Employers Contact Us
Candidates Register your interest

Target Market(s)

IT Professionals in the Philippines & large enterprises in Australia, Singapore and New Zealand

Industry/Entity Type

IT Recruitment

Coding

Coded - Design and coding required

Number of Pages Required

5+ page

Requirements
Must have
• Please based style off logo file attached.

```html
<!DOCTYPE html>
<html lang="en">
<head>
<meta charset="utf-8">
<title>The Remote Tech Specialist – Home</title>
<link rel="stylesheet" href="https://fonts.googleapis.com/css2?family=Montserrat:wght@600;700;800&family=Roboto:wght@400;500;700&family=Roboto+Condensed:wght@600;700&display=swap">
<style>
:root{
  --blue:#1f8fdd;
  --blue-dark:#1674b8;
  --cyan:#7fd3f7;
  --ink:#0d0d0d;
  --text:#555b63;
  --white:#ffffff;
  --pale:#e3f1fb;
  --heading:"Montserrat",sans-serif;
  --body:"Roboto",sans-serif;
  --cond:"Roboto Condensed",sans-serif;
}
*{box-sizing:border-box;margin:0;padding:0}
html,body{width:1200px;height:4415px;overflow:hidden}
body{position:relative;background:var(--white);font-family:var(--body);color:var(--ink)}
section,header,footer,.cta{position:absolute;left:0;width:1200px}
.abs{position:absolute}
.btn{position:absolute;display:flex;align-items:center;justify-content:center;gap:8px;border-radius:24px;font:700 13px/1 var(--body);text-transform:uppercase;letter-spacing:.3px;text-decoration:none}
.btn-blue{background:var(--blue);color:var(--white)}
.btn-black{background:var(--ink);color:var(--white)}
.btn-outline{border:2px solid var(--white);color:var(--white)}
.btn-white{background:var(--white);color:var(--ink)}
.arrow-dot{width:13px;height:13px;border-radius:50%;background:currentColor;display:inline-flex;align-items:center;justify-content:center}
.arrow-dot::after{content:"";width:4px;height:4px;border-top:2px solid var(--blue);border-right:2px solid var(--blue);transform:translateX(-1px) rotate(45deg)}
.btn-blue .arrow-dot{background:var(--white)}
.eyebrow{font:700 27px/1 var(--cond);color:var(--blue);text-transform:uppercase}
.title{font:800 34px/1 var(--heading);text-transform:uppercase;color:var(--ink)}
.rule{display:inline-block;height:1px;background:#b9cfe0;vertical-align:middle}
.photo{position:absolute}

/* header */
.site-header{top:0;height:103px;background:var(--white)}
.brand{position:absolute;display:flex;align-items:center;gap:10px;font:800 40px/1 var(--heading);color:var(--blue)}
.brand-mark{width:16px;height:16px;background:var(--blue)}
.brand-sub{font:600 11px/1.15 var(--heading);color:var(--ink);text-transform:uppercase;width:110px}
.main-nav{position:absolute;top:71px;right:113px;display:flex;gap:24px;font:700 13px/1 var(--body);text-transform:uppercase}
.main-nav a{color:var(--ink);text-decoration:none}
.main-nav a.active{color:var(--blue)}

/* hero */
.hero{top:103px;height:548px;overflow:hidden}
.hero-bg{left:0;top:0;width:1200px;height:548px;background:radial-gradient(circle at 840px 170px,#6b4a3a 0,#3a3b44 22%,#1c2533 55%,#0f1a28 100%)}
.hero h1{position:absolute;left:110px;top:85px;font:800 42px/53px var(--heading);color:var(--white);text-transform:uppercase}
.hero h1 .hl{color:var(--cyan)}
.hero h1 .light{font-weight:600}
.hero-sub{position:absolute;left:110px;top:262px;font:700 19px/42px var(--body);color:var(--white);text-transform:uppercase}
.scroll-btn{position:absolute;left:574px;top:471px;width:52px;height:52px;border-radius:50%;background:var(--white);box-shadow:0 3px 10px rgba(0,0,0,.2);display:flex;align-items:center;justify-content:center}

/* about */
.about{top:651px;height:549px;background:linear-gradient(135deg,#eef2f5 0,#ffffff 45%,#f2f4f6 100%)}
.hex{left:110px;top:55px;width:416px;height:446px;clip-path:polygon(50% 0,100% 24%,100% 76%,50% 100%,0 76%,0 24%);background:linear-gradient(180deg,#c3c7cb 0,#9aa0a6 55%,#5c6168 100%)}
.about-text{position:absolute;left:597px;top:106px;width:500px}
.about-text p{margin-top:24px;font:400 14.5px/26px var(--body);color:var(--text)}

/* services */
.services{top:1200px;height:754px;background:var(--blue)}
.services-bg{left:0;top:0;width:1200px;height:754px;background:linear-gradient(180deg,#1e7fc4 0,#1f8fdd 60%)}
.center-head{position:absolute;left:0;width:1200px;text-align:center}
.card{position:absolute;top:271px;width:308px;height:349px;background:var(--white);border-radius:6px;text-align:center}
.card .photo{left:6px;top:6px;width:296px;height:190px;border-radius:4px}
.card-icon{position:absolute;left:126px;top:166px;width:56px;height:56px;border-radius:50%;background:var(--white);display:flex;align-items:center;justify-content:center}
.card h3{position:absolute;top:226px;left:0;width:100%;font:700 16px/1 var(--body);text-transform:uppercase}
.card p{position:absolute;top:252px;left:20px;right:20px;font:400 13.5px/26px var(--body);color:var(--text)}
.card .more{position:absolute;top:315px;left:0;width:100%;font:700 13px/1 var(--body);color:var(--blue);display:flex;justify-content:center;align-items:center;gap:7px}
.card .more .arrow-dot{background:var(--blue)}
.card .more .arrow-dot::after{border-color:var(--white)}

/* jobs */
.jobs{top:1954px;height:720px;background:var(--white)}
.job{position:absolute;left:113px;width:500px;height:110px}
.job-icon{position:absolute;left:0;top:0;width:106px;height:106px;border-radius:34px;background:var(--pale);display:flex;align-items:center;justify-content:center;transform:rotate(0)}
.job-icon.dark{background:var(--ink)}
.job h3{position:absolute;left:129px;top:8px;font:700 20px/1 var(--cond);text-transform:uppercase}
.job h3.active{color:var(--blue)}
.job p{position:absolute;left:129px;top:38px;width:360px;font:400 13.5px/26px var(--body);color:var(--text)}

/* quotes */
.quotes{top:2674px;height:600px}
.q-left{left:0;top:0;width:597px;height:600px;background:var(--blue)}
.q-right{left:597px;top:0;width:603px;height:600px;background:linear-gradient(160deg,#0f1620,#050607)}
.quotes h2{position:absolute;top:113px;font:800 34px/48px var(--heading);color:var(--white);text-transform:uppercase}
.avatar{position:absolute;top:225px;width:68px;height:68px;border-radius:50%;border:3px solid var(--white)}
.person{position:absolute;top:237px;color:var(--white)}
.person b{display:block;font:700 16px/1 var(--cond);text-transform:uppercase}
.person span{display:block;margin-top:14px;font:400 13px/1 var(--body)}
.quote-box{position:absolute;top:317px;height:190px;padding:22px 20px;font:400 14px/24px var(--body);color:var(--white)}
.quote-box.l{left:113px;width:374px;background:var(--blue-dark)}
.quote-box.r{left:710px;width:377px;background:#17191d}
.q-arrow{position:absolute;top:361px;width:52px;height:52px;border-radius:50%;display:flex;align-items:center;justify-content:center}

/* why */
.why{top:3274px;height:754px;background:var(--white)}
.why-icon{position:absolute;width:86px;height:86px;border-radius:50%;border:3px solid var(--ink);background:var(--white);display:flex;align-items:center;justify-content:center}
.why-label{position:absolute;font:700 15px/26px var(--body);text-transform:uppercase}
.why-label.left{text-align:right;width:220px}
.hub{position:absolute;left:470px;top:221px;width:260px;height:260px;border-radius:50%;background:var(--white);box-shadow:0 0 28px rgba(31,143,221,.25);display:flex;align-items:center;justify-content:center;font:800 62px/1 var(--heading);color:var(--blue)}

/* cta */
.cta{top:3900px;left:91px;width:1016px;height:226px;background:var(--blue);z-index:2}
.cta h2{position:absolute;left:55px;top:46px;font:800 36px/1 var(--heading);color:var(--white);text-transform:uppercase}
.cta .tag{position:absolute;top:107px;font:italic 500 12px/1 var(--body);color:var(--white);text-transform:uppercase}

/* footer */
.site-footer{top:4028px;height:387px;background:var(--ink);color:var(--white)}
.site-footer .brand{color:var(--white)}
.site-footer .brand-mark{background:var(--white)}
.site-footer .brand-sub{color:var(--white)}
.copy{position:absolute;left:110px;top:265px;font:400 12px/1 var(--body)}
.f-col{position:absolute;top:165px}
.f-col h4{font:700 15px/1 var(--body);text-transform:uppercase;margin-bottom:20px}
.f-col li{list-style:none;font:400 13.5px/27.5px var(--body)}
.social{display:flex;gap:10px;margin-top:16px}
.social span{width:32px;height:32px;border-radius:50%;background:var(--white)}
</style>
</head>
<body>

<header class="site-header">
  <div class="brand" style="left:110px;top:31px"><span class="brand-mark"></span>TRTS<span class="brand-sub">The Remote Tech Specialist</span></div>
  <a class="btn btn-blue" style="left:677px;top:8px;width:149px;height:44px">Employ us</a>
  <a class="btn btn-black" style="left:831px;top:8px;width:256px;height:44px">Register your interest</a>
  <nav class="main-nav">
    <a class="active">Home</a><a>About us</a><a>Services</a><a>Work with us</a><a>Careers</a><a>Contact us</a>
  </nav>
</header>

<section class="hero">
  <div class="photo hero-bg" role="img" aria-label="Smiling IT professional at a laptop in a modern office with network line graphics"></div>
  <h1><span class="hl">Connecting Philippine</span><br>Talent with <span class="light">Global IT</span><br><span class="light">Opportunities.</span></h1>
  <p class="hero-sub">We're your bridge to top-notch IT professionals<br>for international companies.</p>
  <a class="btn btn-blue" style="left:110px;top:370px;width:150px;height:44px">Employ us</a>
  <a class="btn btn-outline" style="left:265px;top:370px;width:255px;height:44px">Register your interest</a>
  <svg class="abs" style="left:0;top:400px" width="1200" height="148" viewBox="0 0 1200 148">
    <polygon points="560,148 1200,40 1200,148" fill="#1f8fdd"/>
    <polygon points="0,148 600,95 1200,148" fill="#eef2f5"/>
  </svg>
  <div class="scroll-btn"><svg width="16" height="16" viewBox="0 0 16 16" fill="none" stroke="#0d0d0d" stroke-width="2"><path d="M3 3l5 5 5-5M3 8l5 5 5-5"/></svg></div>
</section>

<section class="about">
  <div class="photo hex" role="img" aria-label="Four smiling professionals seated against a concrete wall"></div>
  <div class="about-text">
    <div class="eyebrow">About us <span class="rule" style="width:112px;margin-left:8px"></span></div>
    <h2 class="title" style="margin-top:20px">Remote Tech Specialist</h2>
    <p>Lorem ipsum dolor sit amet, consectetur adipiscing elit, sed do eiusmod tempor incididunt ut labore et dolore magna aliqua. Ut enim ad minim veniam, quis nostrud exercitation ullamco laboris nisi ut aliquip ex ea commodo consequat. Duis aute irure dolor in reprehenderit in voluptate velit esse cillum dolore eu fugiat nulla pariatur. Excepteur sint occaecat cupidatat non proident, sunt in culpa qui officia deserunt mollit anim id est laborum</p>
  </div>
  <a class="btn btn-blue" style="left:597px;top:403px;width:183px;height:43px">Learn more <span class="arrow-dot"></span></a>
</section>

<section class="services">
  <div class="photo services-bg" role="img" aria-label="Blue-tinted office team background"></div>
  <svg class="abs" style="left:0;top:0" width="1200" height="754" viewBox="0 0 1200 754">
    <polygon points="0,0 620,0 0,145" fill="#050607"/>
    <polygon points="0,754 1200,686 1200,754" fill="#ffffff"/>
  </svg>
  <div class="center-head" style="top:155px"><div class="eyebrow" style="color:var(--white)"><span class="rule" style="width:110px;margin-right:20px;background:rgba(255,255,255,.4)"></span>Our services<span class="rule" style="width:130px;margin-left:20px;background:rgba(255,255,255,.4)"></span></div></div>
  <div class="center-head" style="top:195px"><h2 class="title" style="color:var(--white)">What we do</h2></div>

  <article class="card" style="left:117px">
    <div class="photo" role="img" aria-label="Team collaborating around a laptop" style="background:linear-gradient(135deg,#8a6a50,#c89a52 50%,#4d5664)"></div>
    <div class="card-icon"><svg width="34" height="34" viewBox="0 0 34 34" fill="none" stroke="#333" stroke-width="1.5"><circle cx="14" cy="14" r="8"/><path d="M20 20l8 8"/><circle cx="14" cy="12" r="3"/><path d="M9 19c1-3 9-3 10 0"/></svg></div>
    <h3>Recruitment solutions</h3>
    <p>Lorem ipsum dolor sit amet, consectetur adipiscing elit, sed do</p>
    <div class="more">Learn more <span class="arrow-dot"></span></div>
  </article>
  <article class="card" style="left:447px">
    <div class="photo" role="img" aria-label="Professional woman holding a tablet in an office" style="background:linear-gradient(135deg,#5e6f78,#2a2d33 55%,#9aa6ad)"></div>
    <div class="card-icon"><svg width="34" height="34" viewBox="0 0 34 34" fill="none" stroke="#1f8fdd" stroke-width="1.5"><circle cx="17" cy="9" r="4"/><path d="M9 22c0-6 16-6 16 0M6 28h22M10 22v6M24 22v6"/></svg></div>
    <h3>Compliance management</h3>
    <p>Lorem ipsum dolor sit amet, consectetur adipiscing elit, sed do</p>
    <div class="more">Learn more <span class="arrow-dot"></span></div>
  </article>
  <article class="card" style="left:777px">
    <div class="photo" role="img" aria-label="Consultants meeting around a table" style="background:linear-gradient(135deg,#6a4a3a,#a4856a 50%,#3b4048)"></div>
    <div class="card-icon"><svg width="34" height="34" viewBox="0 0 34 34" fill="none" stroke="#333" stroke-width="1.5"><circle cx="15" cy="13" r="5"/><path d="M6 29c0-8 18-8 18 0M22 5h8v6h-5l-3 3z"/></svg></div>
    <h3>Consulting services</h3>
    <p>Lorem ipsum dolor sit amet, consectetur adipiscing elit, sed do</p>
    <div class="more">Learn more <span class="arrow-dot"></span></div>
  </article>
</section>

<section class="jobs">
  <div class="eyebrow abs" style="left:113px;top:78px">Work opportunities <span class="rule" style="width:110px;margin-left:30px"></span></div>
  <h2 class="title abs" style="left:113px;top:120px">Find your dream job</h2>

  <div class="job" style="top:204px">
    <div class="job-icon"><svg width="46" height="46" viewBox="0 0 46 46" fill="none" stroke="#333" stroke-width="1.6"><path d="M5 22L23 7l18 15M10 18v22h26V18"/><rect x="15" y="27" width="10" height="7"/><path d="M13 37h16"/></svg></div>
    <h3>Work from home</h3>
    <p>orem ipsum dolor sit amet, consectetur adipiscing elit, sed do eiusmod tempor incididunt ut labore et</p>
  </div>
  <div class="job" style="top:338px">
    <div class="job-icon dark"><svg width="46" height="46" viewBox="0 0 46 46" fill="none" stroke="#fff" stroke-width="1.6"><path d="M6 22L23 8l17 14M11 18v22h24V18"/><circle cx="23" cy="27" r="4"/><path d="M16 38c1-5 13-5 14 0"/></svg></div>
    <h3 class="active">Work from office</h3>
    <p>orem ipsum dolor sit amet, consectetur adipiscing elit, sed do eiusmod tempor incididunt ut labore et</p>
  </div>
  <div class="job" style="top:472px">
    <div class="job-icon"><svg width="46" height="46" viewBox="0 0 46 46" fill="none" stroke="#333" stroke-width="1.6"><path d="M10 6h20l6 6v18H10z"/><path d="M15 14h14M15 19h14M15 24h8"/><path d="M8 36l7-5 6 4 6-4 8 5-7 5H15z"/></svg></div>
    <h3>Contract opportunities</h3>
    <p>orem ipsum dolor sit amet, consectetur adipiscing elit, sed do eiusmod tempor incididunt ut labore et</p>
  </div>
  <a class="btn btn-blue" style="left:113px;top:609px;width:254px;height:43px">Browse job listings <span class="arrow-dot"></span></a>

  <div class="photo" role="img" aria-label="Smiling businessman in a suit holding a clipboard" style="left:632px;top:125px;width:460px;height:465px;border-radius:6px;background:linear-gradient(180deg,#dcebf7 0,#d2e5f5 40%,#8b8f96 75%,#5b5f66 100%)"></div>
</section>

<section class="quotes">
  <div class="photo q-left" role="img" aria-label="Blue-tinted team background"></div>
  <div class="photo q-right" role="img" aria-label="Dark office background"></div>
  <svg class="abs" style="left:0;top:0" width="1200" height="60" viewBox="0 0 1200 60"><polygon points="0,0 1200,0 1200,0 597,55 0,22" fill="#ffffff"/></svg>
  <h2 style="left:110px">Quote from a<br>happy candidate</h2>
  <h2 style="right:112px;text-align:right">Quote from a<br>satisfied employer</h2>

  <div class="photo avatar" role="img" aria-label="Candidate portrait" style="left:112px;background:linear-gradient(135deg,#b8a08c,#4a4f58)"></div>
  <div class="person" style="left:195px"><b>Mark Reyes</b><span>Lorum Ipsum Dolor Sit Amet</span></div>
  <div class="photo avatar" role="img" aria-label="Employer portrait" style="left:1019px;background:linear-gradient(135deg,#e3a06a,#7a5238)"></div>
  <div class="person" style="right:190px;text-align:right"><b>Mark Reyes</b><span>Lorum Ipsum Dolor Sit Amet</span></div>

  <div class="quote-box l">Lorem ipsum dolor sit amet, consectetur adipiscing elit, sed do eiusmod tempor incididunt ut labore et dolore magna aliqua. Ut enim ad minim veniam, quis nostrud exercitation ullamco laboris nisi ut aliquip ex ea commodo consequat. Duis aute irure dolor in reprehenderit in voluptate velit esse</div>
  <div class="quote-box r">Lorem ipsum dolor sit amet, consectetur adipiscing elit, sed do eiusmod tempor incididunt ut labore et dolore magna aliqua. Ut enim ad minim veniam, quis nostrud exercitation ullamco laboris nisi ut aliquip ex ea commodo consequat. Duis aute irure dolor in reprehenderit in voluptate velit esse</div>

  <div class="q-arrow" style="left:535px;background:var(--white)"><svg width="16" height="16" viewBox="0 0 16 16" fill="none" stroke="#0d0d0d" stroke-width="2"><path d="M8 3L3 8l5 5M13 3L8 8l5 5"/></svg></div>
  <div class="q-arrow" style="left:612px;background:var(--blue)"><svg width="16" height="16" viewBox="0 0 16 16" fill="none" stroke="#fff" stroke-width="2"><path d="M3 3l5 5-5 5M8 3l5 5-5 5"/></svg></div>
</section>

<section class="why">
  <div class="center-head" style="top:73px"><div class="eyebrow"><span class="rule" style="width:125px;margin-right:15px"></span>Why choose us<span class="rule" style="width:125px;margin-left:15px"></span></div></div>
  <div class="center-head" style="top:112px"><h2 class="title" style="font-size:32px">Why TRTS?</h2></div>

  <svg class="abs" style="left:0;top:0" width="1200" height="600" viewBox="0 0 1200 600" fill="none" stroke="#0d0d0d" stroke-width="2" stroke-dasharray="7 5">
    <path d="M424 214h64l35 26"/><path d="M424 346h81"/><path d="M424 492h64l35-38"/>
    <path d="M776 214h-62l-15 26"/><path d="M799 346h-52"/><path d="M776 492h-62l-15-38"/>
    <g fill="#0d0d0d" stroke="none"><circle cx="523" cy="240" r="7"/><circle cx="505" cy="346" r="7"/><circle cx="523" cy="454" r="7"/><circle cx="699" cy="240" r="7"/><circle cx="747" cy="346" r="7"/><circle cx="699" cy="454" r="7"/></g>
  </svg>
  <div class="hub">TRTS</div>

  <div class="why-label left" style="left:94px;top:188px">Ongoing support for candidates</div>
  <div class="why-label left" style="left:94px;top:320px">Ongoing support for employers</div>
  <div class="why-label left" style="left:94px;top:466px">Local contracts for secure partnerships</div>
  <div class="why-label" style="left:903px;top:201px">Legal compliance</div>
  <div class="why-label" style="left:909px;top:333px">Tax management</div>
  <div class="why-label" style="left:903px;top:466px">Expertise in talent<br>recruitment</div>

  <div class="why-icon" style="left:338px;top:171px"><svg width="40" height="40" viewBox="0 0 40 40" fill="none" stroke="#1f8fdd" stroke-width="1.5"><rect x="10" y="6" width="20" height="26" rx="2"/><path d="M14 12h12M14 17h12M14 22h6"/><circle cx="17" cy="28" r="5"/><path d="M21 32l4 4"/></svg></div>
  <div class="why-icon" style="left:338px;top:303px"><svg width="40" height="40" viewBox="0 0 40 40" fill="none" stroke="#1f8fdd" stroke-width="1.5"><rect x="12" y="5" width="16" height="14"/><path d="M16 10h8M16 14h8M4 26l8-5 7 4 7-4 10 5-8 7H12z"/></svg></div>
  <div class="why-icon" style="left:338px;top:449px"><svg width="40" height="40" viewBox="0 0 40 40" fill="none" stroke="#0d0d0d" stroke-width="1.5"><circle cx="20" cy="20" r="5"/><path d="M20 6v9M20 25v9M6 20h9M25 20h9M10 10l6 6M24 24l6 6M30 10l-6 6M16 24l-6 6"/></svg></div>
  <div class="why-icon" style="left:799px;top:171px"><svg width="40" height="40" viewBox="0 0 40 40" fill="none" stroke="#1f8fdd" stroke-width="1.5"><circle cx="20" cy="16" r="7"/><path d="M20 9v-4M20 27v-4M13 16H9M31 16h-4M8 34h24M14 34l2-8h8l2 8"/></svg></div>
  <div class="why-icon" style="left:799px;top:303px"><svg width="40" height="40" viewBox="0 0 40 40" fill="none" stroke="#0d0d0d" stroke-width="1.5"><circle cx="24" cy="15" r="8"/><path d="M20 19l8-8M21 12h.1M27 18h.1"/><path d="M6 34h14v-8H6zM6 30h14"/></svg></div>
  <div class="why-icon" style="left:799px;top:449px"><svg width="40" height="40" viewBox="0 0 40 40" fill="none" stroke="#1f8fdd" stroke-width="1.5"><circle cx="18" cy="15" r="6"/><path d="M7 34c0-9 22-9 22 0"/><circle cx="28" cy="26" r="5"/><path d="M32 30l4 4"/></svg></div>
</section>

<div class="cta">
  <h2>Find the right talent?</h2>
  <span class="tag" style="left:67px">For employers</span>
  <span class="tag" style="left:241px">For job seekers</span>
  <a class="btn btn-white" style="left:55px;top:138px;width:150px;height:44px">Get in touch</a>
  <a class="btn btn-black" style="left:220px;top:138px;width:256px;height:44px">Register your interest</a>
  <div class="photo" role="img" aria-label="Illustration of two people carrying a large briefcase" style="left:612px;top:0;width:377px;height:226px;background:radial-gradient(ellipse at 50% 55%,#6aa9d8 0,#3f9ae0 45%,var(--blue) 75%)"></div>
</div>

<footer class="site-footer">
  <div class="brand" style="left:110px;top:196px"><span class="brand-mark"></span>TRTS<span class="brand-sub">The Remote Tech Specialist</span></div>
  <p class="copy">Copyright@2025 - All Rights Reserved</p>
  <div class="f-col" style="left:477px"><h4>Quick links</h4><ul><li>Home</li><li>About Us</li><li>Services</li><li>Careers</li><li>Contact Us</li></ul></div>
  <div class="f-col" style="left:665px"><h4>Other links</h4><ul><li>Work from Home</li><li>Work from Office</li><li>Contract Opportunities</li></ul></div>
  <div class="f-col" style="left:888px"><h4>Contact us</h4>
    <ul>
      <li><svg width="13" height="10" viewBox="0 0 13 10" style="margin-right:10px"><rect width="13" height="10" fill="#fff"/><path d="M0 0l6.5 5L13 0" fill="none" stroke="#0d0d0d"/></svg>hello@trts-mail.com</li>
      <li><svg width="12" height="12" viewBox="0 0 12 12" style="margin-right:11px"><path d="M2 1l2.5 0 1 3-1.5 1c.7 1.5 1.5 2.3 3 3l1-1.5 3 1V10c0 .6-.5 1-1 1C5 11 1 7 1 2c0-.6.4-1 1-1z" fill="#fff"/></svg>+1 (555) 010 2040</li>
    </ul>
    <div class="social"><span></span><span></span><span></span></div>
  </div>
</footer>

</body>
</html>
```